Silver Heron Staffing Agency

I need to make a brochure/catalogue that represent our company, telling our clients what we do, our values, fields of industry that we taken care of, so they know who we are, what we did, and how we do it.
I do have a logo and simple brochure design before that i really need to upgrade (i will give it as an example on this attachment).

What I want in the new design is :
1. More pictures and little bit of explanation in each industry we work with.
2. Attractive design that make people LOOK at the brochure and not just throw it in the trash.
3. Still use the combination color of the company logo itself, which is Golden Brown.

```html
<!DOCTYPE html>
<html lang="en">
<head>
<meta charset="utf-8">
<title>Silver Heron Staffing Agency – Trifold Brochure</title>
<link href="https://fonts.googleapis.com/css2?family=Montserrat:wght@400;500;600;700;800&display=swap" rel="stylesheet">
<style>
  :root{
    --ink:#141414;
    --gold:#b08c3c;
    --gold-dark:#9c7a2e;
    --paper:#ffffff;
    --stage:#e4e4e4;
    --text:#2a2a2a;
    --muted:#555;
  }
  *{box-sizing:border-box;margin:0;padding:0}
  html,body{width:1200px;height:2290px;overflow:hidden}
  body{background:var(--stage);font-family:"Montserrat",Arial,sans-serif;color:var(--text);position:relative}
  .spread{position:absolute;left:40px;width:1120px;height:704px;display:grid;grid-template-columns:repeat(3,1fr);background:var(--paper);box-shadow:0 4px 14px rgba(0,0,0,.18)}
  .spread--outside{top:400px}
  .spread--inside{top:1186px}
  .panel{position:relative;overflow:hidden;display:flex;flex-direction:column}
  .panel--dark{background:var(--ink);color:#fff}
  .pad{padding:0 34px}
  .heading{font-size:14px;font-weight:700;color:var(--gold);letter-spacing:.3px;text-transform:uppercase;display:inline-block;border-bottom:1.5px solid var(--gold);padding-bottom:2px;margin-bottom:9px}
  .heading--white{color:#fff;border-color:#fff}
  .heading--dark{color:var(--ink);border-color:var(--ink)}
  .heading .accent{color:var(--gold)}
  .body-text{font-size:10px;line-height:1.4;text-align:justify}
  .panel--dark .body-text{color:#f1f1f1}
  /* outside panel 1 */
  .hero-shape{display:block}
  .industries{padding-top:10px}
  .subhead{font-size:13.5px;font-weight:700;color:var(--gold);line-height:1.2;margin:14px 0 14px;text-decoration:underline;text-underline-offset:3px;text-decoration-thickness:1px}
  .icon-grid{display:grid;grid-template-columns:1fr 1fr;row-gap:10px;column-gap:16px}
  .icon-item{display:flex;align-items:center;gap:10px;font-size:10px;font-weight:600}
  .dot{width:24px;height:24px;border-radius:50%;background:var(--gold);flex:none}
  /* outside panel 2 */
  .contact-form{padding-top:44px}
  .locations{margin-top:26px}
  .map{margin-top:12px;display:flex;gap:8px;align-items:flex-start}
  .map-area{width:170px;height:230px;background:linear-gradient(160deg,#f2f2f2,#d8d8d8);border-radius:2px}
  .map-labels{font-size:11px;font-weight:500;color:var(--ink);padding-top:40px;line-height:1.3}
  .map-labels .gap{margin-top:58px}
  .brand-block{margin-top:16px;width:175px;height:76px;background:var(--ink);clip-path:polygon(0 0,72% 0,100% 100%,0 100%);display:flex;align-items:center;padding-left:16px}
  .brand-name{font-size:12px;font-weight:700;color:var(--gold);letter-spacing:.4px}
  .contact-info{margin-top:14px}
  .contact-line{display:flex;align-items:flex-start;gap:10px;font-size:10px;font-weight:500;line-height:1.3;margin-bottom:7px}
  .contact-line svg{flex:none;margin-top:1px}
  /* outside panel 3 */
  .cover-band{height:114px;background:var(--ink);display:flex;align-items:center;justify-content:center;gap:10px}
  .cover-band .mark{width:14px;height:14px;border-radius:50%;background:var(--gold)}
  .cover-band .brand-name{font-size:17px}
  .cover-hex{display:block;margin:6px auto 0}
  .cover-title{text-align:center;font-weight:800;font-size:40px;line-height:1.05;color:var(--ink);margin-top:6px;letter-spacing:.5px}
  .cover-title .accent{color:var(--gold)}
  .cover-rule{width:56px;height:5px;background:var(--gold);margin:8px auto 12px;border-radius:3px}
  .cover-text{text-align:center;font-size:10.2px;line-height:1.35;padding:0 40px}
  .cover-foot{position:absolute;left:32px;right:32px;bottom:16px;border-top:1px solid #999;padding-top:8px;text-align:center;font-size:8.5px}
  /* inside */
  .block{padding:22px 34px 16px}
  .block .body-text{font-size:9.4px;line-height:1.38}
  .block--about{background:var(--ink)}
  .block--culture{background:var(--gold);color:#fff}
  .block--culture .body-text{color:#fff}
  .block--mission{background:var(--ink);flex:1;padding-bottom:96px}
  .cta{position:absolute;left:34px;right:20px;bottom:20px;display:flex;align-items:center;gap:26px}
  .cta-icon{width:58px;height:58px;border-radius:50%;background:var(--gold);display:flex;align-items:center;justify-content:center;flex:none}
  .cta-icon span{width:34px;height:34px;border-radius:50%;border:2px solid #fff}
  .cta-label{font-size:21px;font-weight:700;letter-spacing:.8px;line-height:1.05}
  .panel--light .cta-label{color:var(--ink)}
  .process{padding-top:32px}
  .process .section{margin-bottom:12px}
  .process .body-text{font-size:9.6px;line-height:1.38}
  .industry-label{font-size:12.5px;font-weight:700;color:var(--gold);margin:2px 0 6px}
  .photo-frame{position:relative;height:112px;margin-right:6px}
  .photo-frame .photo{position:absolute;left:0;top:0;right:6px;bottom:6px}
  .photo-frame::after{content:"";position:absolute;left:70px;top:3px;right:0;bottom:0;border:3px solid var(--gold);border-left:none;pointer-events:none}
  .gallery{padding:30px 34px 0}
  .gallery .photo-frame{height:104px;margin-bottom:8px}
  .photo--hotel{background:linear-gradient(120deg,#eceae6,#9c958c)}
  .photo--mail{background:linear-gradient(120deg,#d9b98a,#c24a3c 70%,#e9e4dc)}
  .photo--landfill{background:linear-gradient(180deg,#c9c2b4,#5a4a3a 60%,#3a3028)}
  .photo--farm{background:linear-gradient(120deg,#3f7a36,#9ccf6a 60%,#2f5a2a)}
  .photo--warehouse{background:linear-gradient(120deg,#8a5a3a,#c7c9b0 55%,#55606a)}
</style>
</head>
<body>

<section class="spread spread--outside" aria-label="Brochure outside">
  <div class="panel panel--dark">
    <svg class="hero-shape" width="373" height="370" viewBox="0 0 373 370" role="img" aria-label="Photo of a smiling hotel housekeeper with a service cart in a hallway">
      <defs>
        <linearGradient id="heroWarm" x1="0" y1="0" x2="1" y2="1">
          <stop offset="0" stop-color="#e8e4e0"/>
          <stop offset=".6" stop-color="#a98f7a"/>
          <stop offset="1" stop-color="#6b3a22"/>
        </linearGradient>
      </defs>
      <polygon points="8,0 365,0 365,272 186,362 8,272" fill="url(#heroWarm)" stroke="var(--gold)" stroke-width="5"/>
    </svg>
    <div class="pad industries">
      <h2 class="heading">Industries</h2>
      <p class="body-text">Need industry-leading talent for your organization? Career options that are ideal for your skills and experience? The professionals at Silver Heron Staffing have the tools and knowledge to help you make the perfect match.</p>
      <p class="subhead">Our specialties include staffing for the following industries</p>
      <div class="icon-grid">
        <div class="icon-item"><span class="dot"></span>Warehousing</div>
        <div class="icon-item"><span class="dot"></span>Transportation</div>
        <div class="icon-item"><span class="dot"></span>Hotel</div>
        <div class="icon-item"><span class="dot"></span>Landfill</div>
        <div class="icon-item"><span class="dot"></span>Casino</div>
        <div class="icon-item"><span class="dot"></span>Food Handling</div>
        <div class="icon-item"><span class="dot"></span>Paper Mailing</div>
      </div>
    </div>
  </div>

  <div class="panel panel--light">
    <div class="pad contact-form">
      <h2 class="heading">Contact Form</h2>
      <p class="body-text">Thank you for choosing Silver Heron Staffing. If you have temporary jobs you are hiring for please get in touch with Harbor Enterprise Solution. We are able to help with all your staffing and employment needs.</p>
      <div class="locations">
        <h2 class="heading">Our Locations</h2>
        <div class="map">
          <div class="map-area" role="img" aria-label="Outline map of the eastern United States"></div>
          <div class="map-labels">
            New York<br>Pennsylvania<br>New Jersey<br>Delaware<br>Virginia
            <div class="gap">Georgia</div>
          </div>
        </div>
      </div>
      <div class="brand-block"><span class="brand-name">SILVER HERON Inc.</span></div>
      <div class="contact-info">
        <h2 class="heading">Contact Info</h2>
        <div class="contact-line">
          <svg width="10" height="10" viewBox="0 0 10 10"><path d="M2 1h2l1 2-1.2 1a5 5 0 0 0 2.2 2.2L7 5l2 1v2c0 .6-.4 1-1 1A8 8 0 0 1 1 2c0-.6.4-1 1-1z" fill="var(--gold)"/></svg>
          555-014-2290</div>
        <div class="contact-line">
          <svg width="10" height="12" viewBox="0 0 10 12"><path d="M5 0a4 4 0 0 1 4 4c0 3-4 8-4 8S1 7 1 4a4 4 0 0 1 4-4z" fill="var(--gold)"/><circle cx="5" cy="4" r="1.5" fill="#fff"/></svg>
          <span>48 Linden Ave, suite 210<br>Riverton, NJ 08077</span></div>
        <div class="contact-line">
          <svg width="10" height="8" viewBox="0 0 10 8"><rect width="10" height="8" fill="var(--gold)"/><path d="M0 0l5 4 5-4" stroke="#fff" fill="none"/></svg>
          info@silverheronstaffing.com</div>
        <div class="contact-line">
          <svg width="10" height="10" viewBox="0 0 10 10"><circle cx="5" cy="5" r="4.3" fill="none" stroke="var(--gold)" stroke-width="1.2"/><path d="M.7 5h8.6M5 .7c2 2.5 2 6.1 0 8.6M5 .7c-2 2.5-2 6.1 0 8.6" stroke="var(--gold)" fill="none" stroke-width=".8"/></svg>
          silverheronstaffing.com</div>
      </div>
    </div>
  </div>

  <div class="panel panel--light">
    <div class="cover-band"><span class="mark"></span><span class="brand-name">SILVER HERON Inc.</span></div>
    <svg class="cover-hex" width="340" height="310" viewBox="0 0 340 310" role="img" aria-label="Photo of a businessman touching a glowing interface over a city skyline and world map">
      <defs>
        <linearGradient id="coverBlue" x1="0" y1="0" x2="1" y2="1">
          <stop offset="0" stop-color="#1f3f72"/>
          <stop offset=".55" stop-color="#4d77ad"/>
          <stop offset="1" stop-color="#c7a86a"/>
        </linearGradient>
      </defs>
      <polygon points="88,4 252,4 336,155 252,306 88,306 4,155" fill="url(#coverBlue)" stroke="var(--gold)" stroke-width="5"/>
    </svg>
    <h1 class="cover-title">YOUR<br>BEST WAY<br>TO <span class="accent">SUCCEED</span></h1>
    <div class="cover-rule"></div>
    <p class="cover-text">Our success is based on our unique ability to identify top candidates and the high-quality professional development of our candidates.</p>
    <div class="cover-foot">silverheronstaffing.com</div>
  </div>
</section>

<section class="spread spread--inside" aria-label="Brochure inside">
  <div class="panel panel--dark">
    <div class="block block--about">
      <h2 class="heading heading--white">About Us</h2>
      <p class="body-text">With more than 18 years of experience Silver Heron Staffing provided staffing services to a wide array of locations, all throughout Pennsylvania. Through the last few years we have expanded to 5 other states including New York, New Jersey, Delaware, Virginia and Georgia. Our ethics are a critical building block of our business. Our own success is based on adherence to the highest ethical standards; long-term client relationships, the ability to identify top candidates, and the high-quality professional development of Silver Heron Staffing professionals protecting the confidentiality and interests of clients and candidates.</p>
    </div>
    <div class="block block--culture">
      <h2 class="heading heading--white">Culture</h2>
      <p class="body-text">Silver Heron Staffing believes in equal opportunity for all, regardless of gender, race, ethic, origin, religion, or handicap. The staffing policies and practices of Silver Heron Staffing for our organization, our clients and candidates are fully non-discriminatory. Our employees are our most valuable asset. We strive to create a work environment of professionalism, trust and respect that will continuously provide our staff with motivation, challenge, and professional growth to aim our most important goal; CLIENT SATISFACTION.</p>
    </div>
    <div class="block block--mission">
      <h2 class="heading heading--white">Mission</h2>
      <p class="body-text">Silver Heron Staffing is more than a staffing company; we want to become your business partner. We understand that payroll and employee-service overhead can be one of the largest expenses for your business. Through our partnership-network programs Silver Heron Staffing can help you reduce the hard-costs of your business expenses. We take responsibility for all our placed employees, including payroll taxes and benefits allowing you to focus on running your business.</p>
    </div>
    <div class="cta"><div class="cta-icon"><span></span></div><div class="cta-label">CONNECTING</div></div>
  </div>

  <div class="panel panel--light">
    <div class="pad process">
      <div class="section">
        <h2 class="heading heading--dark">Our <span class="accent">Process</span></h2>
        <p class="body-text">Our screening process includes a thorough interview with each potential candidate to give us insight into the candidate's previous work history, skills, communication abilities and career goals as well as reference checks with their previous employers.</p>
      </div>
      <div class="section">
        <h2 class="heading heading--dark">Our <span class="accent">Process</span></h2>
        <p class="body-text">Silver Heron Staffing's personalized services, expertise and affordable rates are key factors of our success and being our client's choice staffing agency. Our contingent and contract-to-hire employees are looking for flexible careers in New York, New Jersey, Pennsylvania, Delaware, Virginia and Georgia.</p>
      </div>
      <div class="section">
        <h2 class="heading heading--dark">Why <span class="accent">Us?</span></h2>
        <p class="body-text">Silver Heron Staffing's personalized services, expertise and affordable rates are key factors of our success and being our client's choice staffing agency. Our contingent and contract-to-hire employees are looking for flexible careers in New York, New Jersey, Pennsylvania, Delaware, Virginia and Georgia.</p>
      </div>
      <h2 class="heading heading--dark">Industries <span class="accent">We Serve</span></h2>
      <p class="industry-label">Warehousing</p>
      <div class="photo-frame"><div class="photo photo--warehouse" role="img" aria-label="Photo of a warehouse worker in a hard hat and safety vest holding a clipboard"></div></div>
    </div>
    <div class="cta"><div class="cta-icon"><span></span></div><div class="cta-label">OPPORTUNITY</div></div>
  </div>

  <div class="panel panel--light">
    <div class="gallery">
      <p class="industry-label">Hotel</p>
      <div class="photo-frame"><div class="photo photo--hotel" role="img" aria-label="Photo of a housekeeper making a hotel bed"></div></div>
      <p class="industry-label">Paper Mailing</p>
      <div class="photo-frame"><div class="photo photo--mail" role="img" aria-label="Photo of a delivery worker in a red cap carrying a parcel"></div></div>
      <p class="industry-label">Landfill</p>
      <div class="photo-frame"><div class="photo photo--landfill" role="img" aria-label="Photo of a worker in orange gear at a landfill site"></div></div>
      <p class="industry-label">Farming</p>
      <div class="photo-frame"><div class="photo photo--farm" role="img" aria-label="Photo of a farm worker with a clipboard in a greenhouse"></div></div>
    </div>
    <div class="cta"><div class="cta-icon"><span></span></div><div class="cta-label">WITH TODAY'S<br>TOP TALENT</div></div>
  </div>
</section>

</body>
</html>
```